Create a Graphic About YOURSELF and PixelHarbor

PixelHarbor would like you (designers) to create an awesome graphic to promote YOURSELF and your profile on PixelHarbor!

Your graphic should communicate your name, your services and should mention PixelHarbor.

The design should be perfect for sharing on Chatterly. Here's an example of what we'd like http://blog.pixelharbor-example.ca/article/333/pixelharbor-launches-3000-hire-me-social-design-contest

Once you submitted your design, we'd love you to share the design ('advertisement') and promote yourself and PixelHarbor to your friends and potential customers. So make your submissions great and get your friends to vote for your design by 'Liking' it on Chatterly!

Prizes:
$1500 - "PixelHarbor Community" prize awarded to the designer with the most Chatterly 'Likes'
5 x $50 for the next 5 'most liked' designs on Chatterly

$1000 - "Hire Me" prize awarded to the designer who receives the most client invites
5 x $50 for the next 5 'most invited' designers

In summary, this is a great opportunity for you to increase your exposure to PixelHarbor customers and win cash prizes. Show off your design skills and get hired by PixelHarbor customers from around the world!

Target Market(s)

Fans, friends and customers of YOU

Industry/Entity Type

Cash

Requirements
Must have
• 1) Include your PixelHarbor user name on the graphic so customers can find you in the PixelHarbor Designer Directory
2) Include the tagline "Hire Me on PixelHarbor.com!" in your graphic design.
3) Share your design's URL on our Chatterly wall at http://chatterly-example.com/pixelharbor and get your friends to 'like' your design.
Nice to have
• 1) Include a tagline that expresses your design approach/philosophy
2) Artwork dimensions: 403 x 403 px
3) You can submit more than 1 design!
Should not have
• You must own the copyright of any images you use including stock imagery.

```html
<!DOCTYPE html>
<html lang="en">
<head>
<meta charset="utf-8">
<title>duo studio &amp; three's a... PixelHarbor</title>
<link rel="stylesheet" href="https://fonts.googleapis.com/css2?family=Source+Sans+3:ital,wght@0,400;0,600;0,700;1,700&display=swap">
<style>
  :root {
    --paper: #ffffff;
    --ink: #111111;
    --brand-blue: #0b6a93;
    --mist: #dde9f0;
    --mist-soft: #eaf2f6;
    --faint: #e3e8eb;
  }
  html, body {
    margin: 0;
    padding: 0;
    overflow: hidden;
    background: var(--paper);
  }
  .canvas {
    position: relative;
    width: 1200px;
    height: 1200px;
    overflow: hidden;
    background: var(--paper);
    font-family: "Source Sans 3", "Myriad Pro", Arial, sans-serif;
  }
  .tagline {
    position: absolute;
    left: 42px;
    top: 22px;
    margin: 0;
    font-size: 66px;
    font-weight: 400;
    color: var(--ink);
    letter-spacing: -0.5px;
    white-space: nowrap;
    z-index: 2;
  }
  .tagline .username {
    font-weight: 700;
    font-style: italic;
  }
  .tagline .faint-word {
    font-weight: 600;
    color: var(--faint);
  }
  .crowd-artwork {
    position: absolute;
    left: 70px;
    top: 120px;
    width: 1110px;
    height: 920px;
    z-index: 1;
  }
  .headline {
    position: absolute;
    left: 0;
    right: 0;
    top: 330px;
    margin: 0;
    text-align: center;
    font-size: 330px;
    font-weight: 600;
    line-height: 1;
    letter-spacing: -6px;
    color: var(--brand-blue);
    z-index: 2;
  }
  .hire-line {
    position: absolute;
    right: 28px;
    bottom: 22px;
    margin: 0;
    font-size: 36px;
    font-weight: 400;
    color: var(--ink);
    white-space: nowrap;
    z-index: 2;
  }
  .hire-line .username {
    font-weight: 700;
    font-style: italic;
  }
  .hire-line .site-name {
    font-weight: 700;
    color: var(--brand-blue);
  }
</style>
</head>
<body>
  <main class="canvas">
    <p class="tagline"><span class="username">duo studio</span> &amp; three's a... <span class="faint-word">Pixel</span></p>

    <svg class="crowd-artwork" viewBox="0 0 1110 920" role="img" aria-label="Large pale blue illustration of a crowd of figures bursting outward, behind the headline">
      <defs>
        <radialGradient id="mistGlow" cx="50%" cy="50%" r="50%">
          <stop offset="0%" stop-color="var(--mist)"/>
          <stop offset="70%" stop-color="var(--mist)"/>
          <stop offset="100%" stop-color="var(--mist-soft)" stop-opacity="0"/>
        </radialGradient>
      </defs>
      <ellipse cx="555" cy="460" rx="555" ry="460" fill="url(#mistGlow)"/>
    </svg>

    <h1 class="headline">Harbor</h1>

    <p class="hire-line">Hire <span class="username">duo studio</span> on <span class="site-name">PixelHarbor</span>.com</p>
  </main>
</body>
</html>
```